Larkholm Partners

Need a new website - see more on larkholmpartners.com

Target Market(s)

Finance industry = conservative design

Coding

Coded - Design and coding required

Number of Pages Required

5+ page

Requirements
Should not have
• Dear all,
• Please avoid pictures of people on the website (except the "team" of course :-)

```html
<!DOCTYPE html>
<html lang="en">
<head>
<meta charset="utf-8">
<title>Larkholm Partners</title>
<link href="https://fonts.googleapis.com/css2?family=Lato:wght@400;700;900&display=swap" rel="stylesheet">
<style>
:root{
  --red:#c91f24;
  --red-dark:#a8161b;
  --ink:#222222;
  --muted:#555555;
  --light:#f3f3f3;
  --footer:#262626;
  --footer-box:#353535;
  --white:#ffffff;
}
*{box-sizing:border-box;margin:0;padding:0}
html,body{width:1200px;height:4306px;overflow:hidden}
body{font-family:'Lato',Arial,sans-serif;color:var(--ink);background:var(--white);position:relative}
.abs{position:absolute}
.btn{position:absolute;display:flex;align-items:center;justify-content:center;border-radius:18px;font-size:14px;font-weight:700}
.btn-red{background:var(--red);color:var(--white)}
.btn-white{background:var(--white);color:var(--red)}
.section-title{position:absolute;left:0;width:1200px;text-align:center;font-size:30px;font-weight:400}
.brand{position:absolute;display:flex;align-items:center;gap:10px}
.brand-mark{width:62px;height:62px;border-radius:50%;background:var(--red)}
.brand-name{color:var(--white);font-size:19px;font-weight:700;line-height:1.05;letter-spacing:.5px}

/* hero */
.hero{top:0;left:0;width:1200px;height:709px;background:linear-gradient(160deg,#1d2430 0%,#4b5766 40%,#9aa6b3 62%,#39424f 100%)}
.hero-menu{left:1058px;top:66px}
.hero-headline{position:absolute;top:348px;left:0;width:1200px;text-align:center;color:var(--white);font-size:30px;font-weight:400;line-height:1.3}
.hero-headline b{font-weight:900}
.hero-arrow{top:353px}
.hero-dots{top:660px;left:0;width:1200px;display:flex;justify-content:center;gap:10px}
.hero-dots span{width:8px;height:8px;border-radius:50%;background:var(--white)}
.hero-dots span.on{background:var(--red)}

/* services */
.services-intro{top:805px;left:200px;width:800px;text-align:center;font-size:14px;line-height:1.4;color:var(--muted)}
.service{position:absolute;text-align:center}
.service h3{font-size:18px;font-weight:700;margin-bottom:10px;line-height:1.2}
.service p{font-size:14px;line-height:1.3;color:var(--muted)}
.service .more{display:block;font-size:14px;margin-top:6px;font-weight:700}
.service-feature{left:445px;top:985px;width:316px;height:278px;background:var(--red);border-radius:14px;color:var(--white);padding-top:32px}
.service-feature p{color:var(--white)}

/* engagements */
.engagements{top:1349px;left:0;width:1200px;height:546px;background:var(--red);color:var(--white)}
.engage-kicker{left:120px;top:108px;font-size:15px}
.engage-title{left:120px;top:130px;font-size:29px;font-weight:400}
.engage-rule{left:120px;top:168px;width:296px;height:2px;background:var(--white)}
.engage-tabs{left:120px;top:176px;font-size:14px;font-weight:700;display:flex;gap:22px}
.engage-tabs span+span{border-left:1px solid rgba(255,255,255,.7);padding-left:22px}
.engage-copy{left:120px;top:214px;width:420px;font-size:14px;line-height:1.32}
.engage-copy p+p{margin-top:14px}
.engage-photo{left:617px;top:43px;width:583px;height:460px;background:linear-gradient(135deg,#dfe5ec 0%,#b9c4d0 45%,#6e7a88 100%)}

/* team */
.team-sub{top:1985px;left:250px;width:700px;text-align:center;font-size:14px;line-height:1.35;color:var(--muted)}
.member{position:absolute;top:2044px;width:222px}
.member-photo{width:222px;height:244px;background:linear-gradient(160deg,#6f6a67,#9c857a 55%,#3d3d3d)}
.member-photo.active{background:var(--red);display:flex;align-items:center;justify-content:center;gap:10px}
.member-photo.active span{width:26px;height:26px;border-radius:50%;background:var(--white)}
.member h4{font-size:18px;font-weight:400;margin-top:18px}
.member small{display:block;font-size:13px;color:var(--muted);margin-top:4px}
.slider-dots{display:flex;justify-content:center;gap:8px;left:0;width:1200px}
.slider-dots span{width:8px;height:8px;border-radius:50%;background:var(--ink)}
.slider-dots span.on{background:var(--red)}

/* news */
.news{top:2426px;left:0;width:1200px;height:503px;background:var(--red);color:var(--white)}
.news .section-title{top:48px;color:var(--white)}
.news-nav{top:40px;left:1030px;display:flex;gap:8px}
.news-item{position:absolute;top:112px;width:225px}
.news-img{width:225px;height:161px}
.news-rule{width:46px;height:3px;background:var(--white);margin-top:28px}
.news-item h4{font-size:14px;font-weight:700;line-height:1.15;margin-top:12px;height:34px;overflow:hidden}
.news-date{display:flex;align-items:center;gap:6px;font-size:14px;font-weight:700;margin-top:10px}

/* clients */
.client{position:absolute;top:3069px;width:179px;height:124px;background:var(--light);display:flex;align-items:center;justify-content:center;gap:8px;font-size:24px;font-weight:900;color:#1a1a1a}
.client i{width:14px;height:14px;background:#1a1a1a;display:block}

/* newsletter */
.newsletter-sub{top:3308px;left:0;width:1200px;text-align:center;font-size:14px}
.newsletter-form{top:3345px;left:322px;width:611px;height:36px;display:flex;border:1px solid #888;border-radius:18px;overflow:hidden}
.newsletter-form span{flex:1;font-size:13px;color:#777;padding:10px 22px}
.newsletter-form b{width:153px;background:var(--red);color:var(--white);font-size:14px;display:flex;align-items:center;justify-content:center}

/* contact & why */
.contact{top:3503px;left:0;width:600px;height:407px;background:var(--red);color:var(--white)}
.contact h5{position:absolute;left:120px;top:48px;font-size:15px;font-weight:700}
.contact .rule{position:absolute;left:120px;top:74px;width:66px;height:2px;background:var(--white)}
.field{position:absolute;background:var(--red-dark);font-size:13px;font-weight:700;padding:12px 14px}
.send{position:absolute;left:120px;top:290px;width:440px;height:34px;background:var(--white);color:var(--red);border-radius:10px;display:flex;align-items:center;justify-content:center;font-size:13px;font-weight:700}
.why{top:3503px;left:600px;width:600px;height:407px;background:var(--light)}
.why h5{position:absolute;left:23px;top:42px;font-size:26px;font-weight:400}
.why p{position:absolute;left:23px;top:88px;width:420px;font-size:14px;line-height:1.3;color:var(--muted)}
.skill{position:absolute;left:23px;width:440px}
.skill-label{display:flex;justify-content:space-between;font-size:13px;font-weight:700}
.skill-label em{font-style:normal;font-weight:400}
.skill-bar{height:3px;background:var(--red);margin-top:10px}

/* footer */
.footer{top:3910px;left:0;width:1200px;height:339px;background:var(--footer);color:var(--white)}
.footer-about{left:89px;top:0;width:287px;height:276px;background:var(--footer-box);padding:45px 30px 0 30px}
.footer-about p{font-size:14px;line-height:1.35;margin-top:22px}
.footer-about b{display:block;font-size:14px;margin-top:10px}
.footer-col{top:98px;font-size:14px}
.footer-col h6{font-size:15px;font-weight:700}
.footer-col .rule{width:36px;height:2px;background:var(--white);margin:8px 0 18px}
.footer-col li{list-style:none;line-height:26px;display:flex;align-items:flex-start;gap:10px}
.footer-col li svg{margin-top:7px;flex:none}
.footer-col .addr{line-height:20px;margin-bottom:8px}
.copyright{top:4249px;left:0;width:1200px;height:57px;display:flex;align-items:center;justify-content:space-between;padding:0 122px 0 120px;font-size:14px}
.social{display:flex;gap:8px}
.social span{width:28px;height:28px;border-radius:50%;background:#111}
</style>
</head>
<body>

<section class="abs hero" role="img" aria-label="Close-up of a modern building facade with curved architectural panels">
  <div class="brand" style="left:120px;top:45px">
    <span class="brand-mark"></span>
    <span class="brand-name">LARKHOLM<br>PARTNERS</span>
  </div>
  <svg class="abs hero-menu" width="26" height="22" viewBox="0 0 26 22"><rect y="2" width="26" height="3" fill="#fff"/><rect y="10" width="26" height="3" fill="#fff"/><rect y="18" width="26" height="3" fill="#fff"/></svg>
  <svg class="abs hero-arrow" style="left:40px" width="30" height="30" viewBox="0 0 30 30"><circle cx="15" cy="15" r="13" fill="none" stroke="#fff" stroke-width="2"/><path d="M17 9l-6 6 6 6" fill="none" stroke="#fff" stroke-width="2.4"/></svg>
  <svg class="abs hero-arrow" style="left:1126px" width="30" height="30" viewBox="0 0 30 30"><circle cx="15" cy="15" r="13" fill="none" stroke="#fff" stroke-width="2"/><path d="M13 9l6 6-6 6" fill="none" stroke="#fff" stroke-width="2.4"/></svg>
  <h1 class="hero-headline"><b>Larkholm Partners</b> is a privately held<br>global investment holding group</h1>
  <a class="btn btn-red" style="left:525px;top:441px;width:150px;height:36px">Read More</a>
  <div class="abs hero-dots"><span class="on"></span><span></span><span></span><span></span></div>
</section>

<h2 class="section-title" style="top:755px">Our Services</h2>
<p class="abs services-intro">We offer a wide range of financial services to privately held and publicly traded companies in the United States,Europe and Asia. Though not limited to, Larkholm focuses on the luxury goods sector,primarily taking companies within the high end consumer industries public, aswell as financing already listed companies.<br>Larkholm Partners is a privately held global investment holding group.</p>
<a class="btn btn-red" style="left:522px;top:896px;width:156px;height:34px">View More</a>

<div class="service" style="left:147px;top:1012px;width:240px">
  <svg width="64" height="44" viewBox="0 0 64 44"><path d="M2 14l14-8 10 4 8-4 12 2 16 8" fill="none" stroke="#222" stroke-width="3.5" stroke-linejoin="round"/><path d="M14 22l14 12c3 3 6 2 8 0l12-12" fill="none" stroke="#222" stroke-width="3.5" stroke-linecap="round"/><path d="M26 12l10 10" stroke="#222" stroke-width="3.5"/></svg>
  <h3 style="margin-top:26px">Private Placements</h3>
  <p>Larkholm Partners efficiently arranges both equity and debt financing by offering new capital to public and private companies.</p>
  <span class="more">Read More..</span>
</div>

<div class="service service-feature">
  <svg width="64" height="44" viewBox="0 0 64 44"><rect x="6" y="26" width="8" height="16" fill="#fff"/><rect x="19" y="18" width="8" height="24" fill="#fff"/><rect x="32" y="12" width="8" height="30" fill="#fff"/><rect x="45" y="4" width="8" height="38" fill="#fff"/><rect x="2" y="41" width="58" height="3" fill="#fff"/></svg>
  <h3 style="margin-top:6px">Reverse Mergers &amp;<br>Alternative Offerings</h3>
  <p style="padding:0 26px">Larkholm Partners assists fast growing privately held companies with easy and affordable access to the publicmarkets in the U.S.</p>
  <span class="more">Read More..</span>
</div>

<div class="service" style="left:850px;top:1010px;width:260px">
  <svg width="56" height="52" viewBox="0 0 56 52"><rect x="4" y="14" width="26" height="36" fill="#222"/><rect x="30" y="2" width="22" height="48" fill="#222"/><g fill="#fff"><rect x="9" y="20" width="5" height="5"/><rect x="19" y="20" width="5" height="5"/><rect x="9" y="31" width="5" height="5"/><rect x="19" y="31" width="5" height="5"/><rect x="36" y="9" width="4" height="5"/><rect x="43" y="9" width="4" height="5"/><rect x="36" y="20" width="4" height="5"/><rect x="43" y="20" width="4" height="5"/><rect x="36" y="31" width="4" height="5"/><rect x="43" y="31" width="4" height="5"/></g></svg>
  <h3 style="margin-top:22px">Mergers &amp; Acquisitions</h3>
  <p>We advise in mergers &amp; acquisitions, roll-up strategies, joint ventures, recapitalizations, operate restructuring, and spin-offs.</p>
  <span class="more">Read More..</span>
</div>

<section class="abs engagements">
  <span class="abs engage-kicker">Larkholm Partners</span>
  <h2 class="abs engage-title">Current Engagements</h2>
  <span class="abs engage-rule"></span>
  <div class="abs engage-tabs"><span>Sparkline</span><span>Keystone Involvement</span><span>Orla</span></div>
  <div class="abs engage-copy">
    <p>Sparkline is a blockchain technology company. Sparkline has invented new technologies that provide high efficiency in the 'check out' registration process. Merchants deploy Sparkline systems to enable single-click impulse purchases with highly automated merchant fulfillment support. Furthermore, Sparkline technologies enhances consumer privacy by completely excluding sensitive data, for example spending authority, thus completely changing the shopping cart paradigm.</p>
    <p>Sparkline merchant systems promote new kinds of checkout in environments totally excluded by conventional on-line and real-world scenarios.</p>
  </div>
  <a class="btn btn-white" style="left:120px;top:446px;width:145px;height:32px">View More</a>
  <div class="abs engage-photo" role="img" aria-label="Business documents with charts and a tablet on a desk"></div>
</section>

<h2 class="section-title" style="top:1948px">Professional Team</h2>
<p class="abs team-sub">Lorem Ipsum is simply dummy text of the on printing and typesetting Epsum is simply the Lorem dummy text ever since the 1500s.</p>
<div class="member" style="left:115px"><div class="member-photo" role="img" aria-label="Portrait of a team member"></div><h4>Professional Team</h4><small>LKP Fund Managers</small></div>
<div class="member" style="left:361px"><div class="member-photo" role="img" aria-label="Portrait of a manager"></div><h4>Manager</h4><small>LKP Fund Managers</small></div>
<div class="member" style="left:606px"><div class="member-photo" role="img" aria-label="Portrait of a team member"></div><h4>Professional Team</h4><small>LKP Fund Managers</small></div>
<div class="member" style="left:851px"><div class="member-photo active" role="img" aria-label="Portrait of a manager with social links"><span></span><span></span><span></span></div><h4>Manager</h4><small>LKP Fund Managers</small></div>
<div class="abs slider-dots" style="top:2382px"><span class="on"></span><span class="on"></span><span></span></div>

<section class="abs news">
  <h2 class="section-title">News</h2>
  <div class="abs news-nav">
    <svg width="22" height="22" viewBox="0 0 22 22"><circle cx="11" cy="11" r="9.5" fill="none" stroke="#fff" stroke-width="1.6"/><path d="M13 7l-4 4 4 4" fill="none" stroke="#fff" stroke-width="1.8"/></svg>
    <svg width="22" height="22" viewBox="0 0 22 22"><circle cx="11" cy="11" r="9.5" fill="none" stroke="#fff" stroke-width="1.6"/><path d="M9 7l4 4-4 4" fill="none" stroke="#fff" stroke-width="1.8"/></svg>
  </div>
  <article class="news-item" style="left:120px">
    <div class="news-img" role="img" aria-label="Bronze statue in front of a stone building" style="background:linear-gradient(160deg,#c9a15a,#6b4e2a 60%,#2e2a26)"></div>
    <div class="news-rule"></div>
    <h4>Borealis Gold Mines, Inc. Announces Letter of Intent</h4>
    <div class="news-date"><svg width="14" height="14" viewBox="0 0 14 14"><circle cx="7" cy="7" r="6" fill="none" stroke="#fff" stroke-width="1.5"/><path d="M7 3.5V7l2.5 1.5" fill="none" stroke="#fff" stroke-width="1.5"/></svg>March 26, 2018</div>
  </article>
  <article class="news-item" style="left:365px">
    <div class="news-img" role="img" aria-label="Stock market price board with a rising line" style="background:linear-gradient(160deg,#e9edf3,#8fa4c0 55%,#30496e)"></div>
    <div class="news-rule"></div>
    <h4>Categories Larkholm Partners Limited Announces Acquisition</h4>
    <div class="news-date"><svg width="14" height="14" viewBox="0 0 14 14"><circle cx="7" cy="7" r="6" fill="none" stroke="#fff" stroke-width="1.5"/><path d="M7 3.5V7l2.5 1.5" fill="none" stroke="#fff" stroke-width="1.5"/></svg>March 26, 2018</div>
  </article>
  <article class="news-item" style="left:611px">
    <div class="news-img" role="img" aria-label="Glowing blue digital technology scene" style="background:linear-gradient(160deg,#0c2a7a,#2d6ae0 55%,#081a4a)"></div>
    <div class="news-rule"></div>
    <h4>Categories LinkTide, Inc. Announces Agreement to Acquire</h4>
    <div class="news-date"><svg width="14" height="14" viewBox="0 0 14 14"><circle cx="7" cy="7" r="6" fill="none" stroke="#fff" stroke-width="1.5"/><path d="M7 3.5V7l2.5 1.5" fill="none" stroke="#fff" stroke-width="1.5"/></svg>March 26, 2018</div>
  </article>
  <article class="news-item" style="left:856px">
    <div class="news-img" role="img" aria-label="City skyline at night" style="background:linear-gradient(180deg,#1b2436,#34425e 55%,#7a5a3a)"></div>
    <div class="news-rule"></div>
    <h4>Larkholm Partners Limited closed the acquisition of a</h4>
    <div class="news-date"><svg width="14" height="14" viewBox="0 0 14 14"><circle cx="7" cy="7" r="6" fill="none" stroke="#fff" stroke-width="1.5"/><path d="M7 3.5V7l2.5 1.5" fill="none" stroke="#fff" stroke-width="1.5"/></svg>March 26, 2018</div>
  </article>
  <a class="btn btn-white" style="left:527px;top:426px;width:146px;height:32px">View More</a>
</section>

<h2 class="section-title" style="top:2998px">Our Client's</h2>
<div class="client" style="left:120px">Sparkline</div>
<div class="client" style="left:316px;font-size:17px"><i></i>KEYSTONE</div>
<div class="client" style="left:511px;font-size:30px">ORLA</div>
<div class="client" style="left:706px">Sparkline</div>
<div class="client" style="left:901px;font-size:17px"><i></i>KEYSTONE</div>

<h2 class="section-title" style="top:3266px;font-size:25px">Join Our Newletter</h2>
<p class="abs newsletter-sub">Sign up for Our Newsletter</p>
<div class="abs newsletter-form"><span>Email Here</span><b>SUBSCRIBE</b></div>

<section class="abs contact">
  <h5>QUICK CONTACT</h5>
  <span class="rule"></span>
  <div class="field" style="left:120px;top:108px;width:213px;height:44px">Name</div>
  <div class="field" style="left:347px;top:108px;width:213px;height:44px">Phone</div>
  <div class="field" style="left:120px;top:170px;width:440px;height:94px">Message</div>
  <div class="send">SEND</div>
</section>

<section class="abs why">
  <h5>Why Choose US?</h5>
  <p>Lorem Ipsum is simply dummy text of the on printing and typesetting Epsum is simply the Lorem dummy text ever since the 1500s.</p>
  <div class="skill" style="top:158px"><div class="skill-label">FINANCIAL ANALYSIS<em>95%</em></div><div class="skill-bar" style="width:418px"></div></div>
  <div class="skill" style="top:212px"><div class="skill-label">INVESTMENTS<em>92%</em></div><div class="skill-bar" style="width:405px"></div></div>
  <div class="skill" style="top:264px"><div class="skill-label">FINANCIAL PLANNER<em>70%</em></div><div class="skill-bar" style="width:308px"></div></div>
  <div class="skill" style="top:322px"><div class="skill-label">BUSINESS SUPPORT<em>75%</em></div><div class="skill-bar" style="width:330px"></div></div>
</section>

<footer class="abs footer">
  <div class="abs footer-about">
    <div class="brand" style="position:static">
      <span class="brand-mark" style="width:54px;height:54px"></span>
      <span class="brand-name" style="font-size:17px">LARKHOLM<br>PARTNERS</span>
    </div>
    <p>Lorem Ipsum is simply dummy text of the printing and typesetting industry. Lorem Ipsum has been the industry's standard.</p>
    <b>Read More..</b>
  </div>
  <div class="abs footer-col" style="left:428px">
    <h6>QUICK LINK</h6><div class="rule"></div>
    <ul>
      <li><svg width="7" height="10" viewBox="0 0 7 10"><path d="M1 1l4 4-4 4" fill="none" stroke="#fff" stroke-width="1.6"/></svg>Home</li>
      <li><svg width="7" height="10" viewBox="0 0 7 10"><path d="M1 1l4 4-4 4" fill="none" stroke="#fff" stroke-width="1.6"/></svg>Services</li>
      <li><svg width="7" height="10" viewBox="0 0 7 10"><path d="M1 1l4 4-4 4" fill="none" stroke="#fff" stroke-width="1.6"/></svg>News</li>
      <li><svg width="7" height="10" viewBox="0 0 7 10"><path d="M1 1l4 4-4 4" fill="none" stroke="#fff" stroke-width="1.6"/></svg>Teams</li>
      <li><svg width="7" height="10" viewBox="0 0 7 10"><path d="M1 1l4 4-4 4" fill="none" stroke="#fff" stroke-width="1.6"/></svg>Contact</li>
    </ul>
  </div>
  <div class="abs footer-col" style="left:594px;width:230px">
    <h6>BEVERLY HILLS</h6><div class="rule"></div>
    <ul>
      <li class="addr"><svg width="12" height="15" viewBox="0 0 12 15"><path d="M6 14S1 8.5 1 5.5a5 5 0 0110 0C11 8.5 6 14 6 14z" fill="#fff"/><circle cx="6" cy="5.5" r="1.8" fill="#262626"/></svg>212 Marlow Avenue - Suite 410 Beverly Hills, CA 90211, United States</li>
      <li><svg width="13" height="13" viewBox="0 0 13 13"><path d="M3 1l2 3-1.5 1.5a7 7 0 004 4L9 8l3 2-1 2.5C6 13 0 7 .5 2z" fill="#fff"/></svg>+1 310 555 0142</li>
      <li><svg width="14" height="10" viewBox="0 0 14 10"><rect width="14" height="10" rx="1" fill="#fff"/><path d="M1 1l6 4.5L13 1" fill="none" stroke="#262626" stroke-width="1.2"/></svg>info@larkholmpartners.com</li>
    </ul>
  </div>
  <div class="abs footer-col" style="left:850px;width:240px">
    <h6>LONDON</h6><div class="rule"></div>
    <ul>
      <li class="addr"><svg width="12" height="15" viewBox="0 0 12 15"><path d="M6 14S1 8.5 1 5.5a5 5 0 0110 0C11 8.5 6 14 6 14z" fill="#fff"/><circle cx="6" cy="5.5" r="1.8" fill="#262626"/></svg>18 Harrow Row<br>SW1A 4LK London<br>United Kingdom</li>
      <li><svg width="13" height="13" viewBox="0 0 13 13"><path d="M3 1l2 3-1.5 1.5a7 7 0 004 4L9 8l3 2-1 2.5C6 13 0 7 .5 2z" fill="#fff"/></svg>+44 (0) 20 7946 0321</li>
      <li><svg width="14" height="10" viewBox="0 0 14 10"><rect width="14" height="10" rx="1" fill="#fff"/><path d="M1 1l6 4.5L13 1" fill="none" stroke="#262626" stroke-width="1.2"/></svg>info@larkholmpartners.com</li>
    </ul>
  </div>
</footer>

<div class="abs copyright">
  <span>Copyright © 2018 Larkholm Partners. All Rights Reserved.</span>
  <div class="social"><span></span><span></span><span></span><span></span><span></span></div>
</div>

</body>
</html>
```